VELNUKA Promotions - Business Card Design Project

We are looking for a classy business cards for Promotion Company based in Toronto, Canada named Velnuka Promotions.

Velnuka Promotions has an idea and vision to set high standard, be EXCLUSIVE and attract a group of people that will follow us through events we promote (night clubs, brand promotions, music events, and sport events)

We want to present a high standards and classy image to the others...
Updates

Target Market(s)

male/female age 25-40 Target: business owners young entrepreneur - clubing industry - media industry - promotion industry - marketing media industry

Industry/Entity Type

Events

Requirements
Must have
• business cards should be classy, make people feel exclusive , make people react ..

```html
<!DOCTYPE html>
<html lang="en">
<head>
<meta charset="utf-8">
<title>Velnuka Promotions – Business Card</title>
<link href="https://fonts.googleapis.com/css2?family=Montserrat:wght@400;700&family=Open+Sans:wght@400;600&display=swap" rel="stylesheet">
<style>
  :root {
    --page-bg: #ffffff;
    --card-light: #5c5c5c;
    --card-mid: #3a3a3a;
    --card-dark: #1c1c1c;
    --accent-blue: #1ea9e1;
    --text-white: #ffffff;
    --text-soft: #e6e6e6;
    --watermark: rgba(255, 255, 255, 0.11);
  }
  html, body {
    margin: 0;
    padding: 0;
    width: 1200px;
    height: 900px;
    overflow: hidden;
    background: var(--page-bg);
  }
  .canvas {
    position: relative;
    width: 1200px;
    height: 900px;
  }
  .business-card {
    position: absolute;
    left: 130px;
    top: 168px;
    width: 940px;
    height: 564px;
    overflow: hidden;
    background: radial-gradient(ellipse 70% 80% at 50% 22%, var(--card-light) 0%, var(--card-mid) 45%, var(--card-dark) 100%);
  }
  .brand-name {
    position: absolute;
    left: 0;
    width: 100%;
    top: 92px;
    text-align: center;
    font-family: "Montserrat", sans-serif;
    font-weight: 400;
    color: var(--accent-blue);
    line-height: 1;
  }
  .brand-name .brand-main {
    display: block;
    font-size: 64px;
    letter-spacing: 4px;
  }
  .brand-name .brand-sub {
    display: block;
    margin-top: 8px;
    font-size: 17px;
    letter-spacing: 9px;
    padding-left: 150px;
  }
  .brand-watermark {
    position: absolute;
    left: 2px;
    bottom: -38px;
    font-family: "Montserrat", sans-serif;
    font-weight: 400;
    font-size: 200px;
    letter-spacing: 6px;
    line-height: 1;
    color: var(--watermark);
    white-space: nowrap;
  }
  .person {
    position: absolute;
    right: 510px;
    top: 284px;
    text-align: right;
  }
  .person-name {
    margin: 0;
    font-family: "Montserrat", sans-serif;
    font-weight: 700;
    font-size: 46px;
    line-height: 1;
    color: var(--text-white);
  }
  .person-name .surname { color: var(--accent-blue); }
  .person-role {
    margin: 10px 0 0;
    font-family: "Open Sans", sans-serif;
    font-size: 18px;
    color: var(--text-soft);
  }
  .person-role .company { color: var(--accent-blue); }
  .divider {
    position: absolute;
    left: 470px;
    top: 262px;
    width: 2px;
    height: 132px;
    background: var(--accent-blue);
  }
  .contact-list {
    position: absolute;
    left: 492px;
    top: 284px;
    margin: 0;
    padding: 0;
    list-style: none;
    font-family: "Open Sans", sans-serif;
    font-size: 18px;
    color: var(--text-soft);
  }
  .contact-list li { height: 33px; line-height: 24px; }
  .contact-list .label { color: var(--text-soft); }
  .contact-list .label-blue { color: var(--accent-blue); }
  .contact-list .highlight { color: var(--accent-blue); }
</style>
</head>
<body>
<div class="canvas">
  <section class="business-card" aria-label="Velnuka Promotions business card">
    <div class="brand-watermark" aria-hidden="true">VELNUKA</div>

    <div class="brand-name">
      <span class="brand-main">VELNUKA</span>
      <span class="brand-sub">PROMOTIONS</span>
    </div>

    <div class="person">
      <h1 class="person-name">Marco <span class="surname">Lenz</span></h1>
      <p class="person-role">CEO <span class="company">Velnuka</span> Promotion</p>
    </div>

    <div class="divider"></div>

    <ul class="contact-list">
      <li><span class="label-blue">tel:</span> +1 416 <span class="highlight">555</span> 0192</li>
      <li><span class="label">email :</span> <span class="highlight">marco</span>@velnuka.com</li>
      <li><span class="label-blue">web:</span> www.<span class="highlight">velnuka</span>.com</li>
    </ul>
  </section>
</div>
</body>
</html>
```